Business Card

I need a business card that really pops for a potential customer or person who refers a personal injury lead. I want to highlight our office locations, but only address that needs to be on the card is my office's main address. I want a sleek, modern and minimalist design.

```html
<!DOCTYPE html>
<html lang="en">
<head>
<meta charset="utf-8">
<title>Kestrel Injury Lawyers – Business Card</title>
<link rel="stylesheet" href="https://fonts.googleapis.com/css2?family=Montserrat:wght@400;600&display=swap">
<style>
  :root {
    --page-bg: #161616;
    --card-bg: #323232;
    --ink: #f4f4f4;
    --ink-soft: #e2e2e2;
    --rule: #d8d8d8;
    --emboss: #4a4a4a;
  }
  * { margin: 0; padding: 0; box-sizing: border-box; }
  html, body {
    width: 1200px;
    height: 1059px;
    overflow: hidden;
    background: var(--page-bg);
    font-family: "Montserrat", sans-serif;
    color: var(--ink);
  }
  .canvas { position: relative; width: 1200px; height: 1059px; }
  .card {
    position: absolute;
    background: var(--card-bg);
    border-radius: 18px;
  }
  .card--front { left: 257px; top: 89px; width: 687px; height: 390px; }
  .card--back  { left: 254px; top: 547px; width: 693px; height: 393px; }

  .firm-name {
    position: absolute;
    font-family: "Montserrat", sans-serif;
    font-weight: 600;
    letter-spacing: 0;
    white-space: nowrap;
  }
  .card--front .firm-name {
    right: 39px; top: 66px;
    font-size: 24px; line-height: 30px;
    color: var(--ink);
  }
  .card--back .firm-name {
    left: 0; right: 0; top: 170px;
    text-align: center;
    font-size: 40px; line-height: 50px;
    color: var(--emboss);
  }

  .person { position: absolute; left: 39px; top: 195px; }
  .person__name { font-size: 25px; font-weight: 600; letter-spacing: 0.6px; line-height: 30px; }
  .person__role { font-size: 15px; font-weight: 400; color: var(--ink-soft); margin-top: 3px; }

  .rule {
    position: absolute; left: 39px; right: 39px; top: 264px;
    height: 1px; background: var(--rule);
  }

  .contacts { position: absolute; left: 39px; top: 282px; list-style: none; }
  .contacts li {
    display: flex; align-items: center; gap: 8px;
    font-size: 16px; font-weight: 400; letter-spacing: 0.4px;
    height: 25px;
  }
  .contacts svg { width: 12px; height: 12px; fill: var(--ink); flex: none; }

  .address-divider {
    position: absolute; left: 284px; top: 313px;
    width: 1px; height: 38px; background: var(--rule);
  }
  .address {
    position: absolute; left: 299px; top: 309px;
    font-style: normal; font-size: 16px; letter-spacing: 0.4px; line-height: 22px;
  }
</style>
</head>
<body>
<main class="canvas">
  <section class="card card--front" aria-label="Card front">
    <p class="firm-name">Kestrel Injury Lawyers</p>

    <div class="person">
      <p class="person__name">DANIEL BROOKS</p>
      <p class="person__role">CEO/Founder</p>
    </div>

    <div class="rule"></div>

    <ul class="contacts">
      <li>
        <svg viewBox="0 0 12 12" aria-hidden="true"><path d="M1 4.5C1 2.5 3.5 1.5 6 1.5S11 2.5 11 4.5L9 5 8.5 3.8H3.5L3 5zM3 6h6l1.5 4.5h-9z"/></svg>
        (555) 014 2378
      </li>
      <li>
        <svg viewBox="0 0 12 12" aria-hidden="true"><path d="M1 5 6 1.5 11 5v6H1z M2 5.6 6 8.4 10 5.6" stroke="#323232" stroke-width="0.8"/></svg>
        info@kestrelinjury.com
      </li>
      <li>
        <svg viewBox="0 0 12 12" aria-hidden="true"><circle cx="6" cy="6" r="5.2"/><path d="M3 3.5 5 4 4.5 6 6 7.5 5.5 10M8 2.5 7.5 4.5 9.5 6" stroke="#323232" stroke-width="1" fill="none"/></svg>
        www.kestrelinjury.com
      </li>
    </ul>

    <div class="address-divider"></div>
    <address class="address">
      2716 Larkspur Ave<br>
      Fairview Springs, 40213
    </address>
  </section>

  <section class="card card--back" aria-label="Card back">
    <p class="firm-name">Kestrel Injury Lawyers</p>
  </section>
</main>
</body>
</html>
```